Barrister at Law needs Business Card Design

Need a business card design for Barrister at Law. Double sided. Simple Miles Tordoff and Barrister at Law on one side with contact details on the other side. I would like a professional design using Black or Platinum. Details on reverse side would include qualifications - Bcom-Llb and Acc Spec Commercial Litigation. I have attached the logo. Contact details would include address/ Po Box/ Phone/Fax/Mobile/email. I would like to use raised print or spot gloss.

```html
<!DOCTYPE html>
<html lang="en">
<head>
<meta charset="utf-8">
<title>Miles Tordoff – Barrister at Law business card</title>
<link href="https://fonts.googleapis.com/css2?family=Open+Sans:wght@400;600&display=swap" rel="stylesheet">
<style>
  :root {
    --backdrop: #d9d6d1;
    --paper: #ebe9e5;
    --ink: #121212;
    --ink-soft: #2b2b2b;
    --accent: #2fa7dc;
    --on-dark: #ffffff;
    --on-dark-soft: #dfe9f0;
    --badge-line: #8e8c88;
  }
  * { margin: 0; padding: 0; box-sizing: border-box; }
  html, body { width: 1200px; height: 918px; overflow: hidden; }
  body {
    background: var(--backdrop);
    font-family: "Open Sans", Arial, sans-serif;
    position: relative;
  }
  .card {
    position: absolute;
    left: 280px;
    width: 640px;
    height: 366px;
    background: var(--paper);
    box-shadow: 0 6px 18px rgba(0,0,0,.18);
    overflow: hidden;
  }
  .card--back { top: 60px; }
  .card--front { top: 492px; }

  .brand-name {
    position: absolute;
    inset: 0;
    display: flex;
    align-items: center;
    justify-content: center;
    font-size: 34px;
    font-weight: 600;
    color: var(--ink);
    letter-spacing: .5px;
  }

  .card__swoosh { position: absolute; inset: 0; }

  .accreditation-badge {
    position: absolute;
    left: 42px;
    top: 26px;
  }

  .identity {
    position: absolute;
    right: 32px;
    top: 52px;
    text-align: right;
    color: var(--on-dark);
  }
  .identity__name { font-size: 24px; font-weight: 600; line-height: 1.2; }
  .identity__quals {
    font-size: 15px;
    color: var(--on-dark-soft);
    line-height: 1.35;
    margin-top: 4px;
  }

  .contact-list {
    position: absolute;
    left: 34px;
    top: 222px;
    list-style: none;
    font-size: 14px;
    color: var(--ink-soft);
  }
  .contact-list li {
    display: flex;
    align-items: center;
    gap: 8px;
    height: 24px;
  }
  .contact-list svg { width: 14px; height: 14px; fill: var(--accent); }

  .address {
    position: absolute;
    left: 250px;
    top: 270px;
    font-size: 14px;
    line-height: 1.5;
    color: var(--ink-soft);
    font-style: normal;
  }
</style>
</head>
<body>

  <section class="card card--back" aria-label="Card back">
    <div class="brand-name">Tordoff Chambers</div>
  </section>

  <section class="card card--front" aria-label="Card front">
    <svg class="card__swoosh" viewBox="0 0 640 366" width="640" height="366" aria-hidden="true">
      <path d="M408 0 C338 60 362 160 456 262 C506 316 528 340 546 366 L640 366 L640 0 Z" fill="var(--accent)"/>
      <path d="M418 0 C350 60 374 160 466 262 C516 316 538 340 556 366 L640 366 L640 0 Z" fill="var(--ink)"/>
    </svg>

    <svg class="accreditation-badge" width="170" height="170" viewBox="0 0 170 170" role="img" aria-label="Accreditation badge">
      <circle cx="85" cy="85" r="80" fill="none" stroke="var(--badge-line)" stroke-width="2"/>
    </svg>

    <div class="identity">
      <div class="identity__name">Miles Tordoff</div>
      <div class="identity__quals">Bcom-Llb&amp;Acc.Spec.<br>(Comm Lit)</div>
    </div>

    <ul class="contact-list">
      <li>
        <svg viewBox="0 0 24 24"><path d="M6.6 10.8a15.1 15.1 0 0 0 6.6 6.6l2.2-2.2a1 1 0 0 1 1-.25 11.4 11.4 0 0 0 3.6.57 1 1 0 0 1 1 1V20a1 1 0 0 1-1 1A17 17 0 0 1 3 4a1 1 0 0 1 1-1h3.5a1 1 0 0 1 1 1c0 1.25.2 2.45.57 3.6a1 1 0 0 1-.25 1z"/></svg>
        612 555 0148
      </li>
      <li>
        <svg viewBox="0 0 24 24"><path d="M7 1h10a2 2 0 0 1 2 2v18a2 2 0 0 1-2 2H7a2 2 0 0 1-2-2V3a2 2 0 0 1 2-2zm0 3v14h10V4zm5 15.5a1.2 1.2 0 1 0 0 2.4 1.2 1.2 0 0 0 0-2.4z"/></svg>
        612 555 0372
      </li>
      <li>
        <svg viewBox="0 0 24 24"><path d="M6 2h9l3 3v5H6zm-2 9h16a2 2 0 0 1 2 2v6h-4v3H6v-3H2v-6a2 2 0 0 1 2-2zm4 6v3h8v-3z"/></svg>
        612 555 0916
      </li>
      <li>
        <svg viewBox="0 0 24 24"><path d="M2 5h20v14H2zm2 2v.5l8 5 8-5V7zm0 2.8V17h16V9.8l-8 5z"/></svg>
        miles@tordoffchambers.com
      </li>
    </ul>

    <address class="address">
      14 Wattlebank Row<br>
      Brindlewood, QLD 4172<br>
      www.tordoffchambers.com
    </address>
  </section>

</body>
</html>
```